Website for enterprise software start-up

We need a new Wordpress website. We are an early stage start-up focused on mobile video technology for cellular operators. The audience is strategy, marketing and customer acquisition execs from the operators.

The purpose of the site is to act as a sales brochure and capture leads. A demo app can be downloaded from the current site, want to put that behind a contact form.

Current website is at www.brellowmo.tv. Similar number of pages. Looking for a clean design template, with minimal customization. Blog will remain as is.

Want to be able to modify the copy via Wordpress. Reference designs I like: vandrisk.com, tallowquarrymetric.com

Target Market(s)

Mobile operators and MVNOs in the US and Asia Pacific regions

Industry/Entity Type

Business Software

Coding

Coded - Design and coding required

Number of Pages Required

4 page

Font styles to use
Sans Serif

Colors
f78f20

Requirements
Must have
• Form for downloading sample apps.
• Landing page with image, Product, Blog, About, Contact
• Team page

```html
<!DOCTYPE html>
<html lang="en">
<head>
<meta charset="utf-8">
<title>Brellowmo Media</title>
<link href="https://fonts.googleapis.com/css2?family=Josefin+Sans:wght@300;400&family=Open+Sans:wght@400;600;700&display=swap" rel="stylesheet">
<style>
:root{
  --orange:#f78f20;
  --ink:#2b2b2b;
  --text:#666;
  --muted:#999;
  --line:#e6e6e6;
  --card:#efefef;
  --dark:#1c1c1c;
  --white:#fff;
}
*{box-sizing:border-box;margin:0;padding:0}
html,body{width:1200px;height:4580px;overflow:hidden}
body{position:relative;background:var(--white);font-family:"Open Sans",Arial,sans-serif;color:var(--text)}
.abs{position:absolute}
.display{font-family:"Josefin Sans",Arial,sans-serif;font-weight:300}

/* header */
.site-header{position:absolute;left:0;top:0;width:1200px;height:85px;background:var(--white);border-bottom:1px solid var(--line)}
.brand{position:absolute;display:flex;align-items:center;gap:12px;font-family:"Open Sans",Arial,sans-serif;font-weight:700;font-size:30px;color:var(--ink);letter-spacing:-.5px;white-space:nowrap}
.brand-mark{width:40px;height:40px;background:var(--orange)}
.site-header .brand{left:76px;top:20px}
.main-nav{position:absolute;top:34px;left:412px;display:flex}
.main-nav a{font-size:13px;color:var(--ink);text-decoration:none;text-transform:uppercase;font-weight:600;margin-right:38px}
.header-btn{position:absolute;top:0;height:85px;color:var(--white);font-size:13px;font-weight:700;text-transform:uppercase;display:flex;flex-direction:column;align-items:center;justify-content:center;gap:6px}
.header-btn i{width:18px;height:18px;border:2px solid var(--white);border-radius:50%}
.btn-login{left:878px;width:128px;background:#111}
.btn-apps{left:1006px;width:114px;background:var(--orange)}

/* hero */
.hero{position:absolute;left:0;top:85px;width:1200px;height:623px;background:linear-gradient(100deg,#2a1d14 0%,#6b4a32 35%,#c9a584 62%,#e9ddd0 100%)}
.hero-copy{position:absolute;left:76px;top:205px;padding:0 0 0 28px;border-left:4px solid var(--orange)}
.hero-copy h1{font-family:"Josefin Sans",Arial,sans-serif;font-weight:300;font-size:44px;line-height:50px;color:var(--white)}
.hero-copy h1 span{color:var(--orange)}
.hero-copy p{margin-top:14px;width:360px;font-size:17px;line-height:26px;color:var(--white)}
.btn{display:inline-flex;align-items:center;gap:10px;background:var(--orange);color:var(--white);font-size:14px;font-weight:700;text-transform:uppercase;padding:0 26px;height:46px}
.btn b{width:20px;height:20px;border-radius:50%;background:var(--white);color:var(--orange);font-size:13px;display:flex;align-items:center;justify-content:center}
.hero-copy .btn{margin-top:28px}

/* welcome */
.welcome{position:absolute;left:0;top:708px;width:1200px;height:212px;border-bottom:1px solid var(--line)}
.welcome-title{position:absolute;left:76px;top:72px;font-size:20px;color:var(--ink)}
.welcome-title strong{display:block;font-weight:300;color:var(--orange);font-size:36px;line-height:44px}
.welcome-rule{position:absolute;left:390px;top:38px;width:3px;height:128px;background:var(--orange)}
.welcome-text{position:absolute;left:433px;top:44px;width:690px;font-size:16px;line-height:26px}

/* section headings */
.section-title{font-family:"Josefin Sans",Arial,sans-serif;font-weight:300;color:var(--orange);font-size:40px;line-height:48px}
.section-sub{font-size:17px;line-height:26px;color:var(--text)}
.center{text-align:center;width:1200px;left:0}

/* push */
.feature{position:absolute;font-size:16px;line-height:26px;width:330px}
.device{position:absolute;border-radius:40px;background:#2f2f31}
.device .screen{position:absolute;left:14px;right:14px;top:80px;bottom:80px;background:linear-gradient(160deg,#6f8a5c,#3c4a34)}
.divider{position:absolute;left:0;width:1200px;height:1px;background:var(--line)}

/* native */
.feature-list{position:absolute;font-size:15px;line-height:24px;width:280px;padding-left:26px}
.feature-list::before{content:"";position:absolute;left:0;top:6px;width:10px;height:10px;border-top:2px solid var(--orange);border-right:2px solid var(--orange);transform:rotate(45deg)}

/* blog */
.blog-feature{position:absolute;left:76px;top:2638px;width:512px;height:372px;background:linear-gradient(180deg,#e9b887 0%,#b88c6c 45%,#3a3a3c 100%)}
.blog-feature figcaption{position:absolute;left:0;bottom:0;width:100%;height:68px;background:rgba(247,143,32,.92);color:var(--white);padding:12px 22px}
.blog-feature h3{font-size:17px;font-weight:600}
.meta{font-size:12px;margin-top:4px}
.meta em{font-style:normal;color:var(--orange)}
.blog-feature .meta em{color:var(--white)}
.blog-card{position:absolute;width:238px;height:110px;background:var(--card);padding:14px 16px}
.blog-card h3{font-size:15px;line-height:21px;font-weight:400;color:var(--ink)}
.blog-card .meta{color:var(--muted)}

/* team */
.team-copy{position:absolute;left:76px;top:3180px;width:490px}
.team-copy p{margin-top:26px;font-size:15px;line-height:25px}
.team-copy .btn{margin-top:34px;height:44px;font-size:13px}
.member{position:absolute;border-radius:50%;border:6px solid #f9b46a;background:linear-gradient(180deg,#d7cfc6,#8f877f)}

/* apps band */
.apps-band{position:absolute;left:0;top:3697px;width:1200px;height:427px;background:linear-gradient(110deg,#5c5a55 0%,#a89a88 40%,#6d6660 70%,#2e2b29 100%)}
.apps-band .section-title{position:absolute;top:145px;font-size:46px}
.apps-band p{position:absolute;top:200px;color:var(--white);font-size:17px}
.store-badge{position:absolute;top:231px;width:202px;height:62px;background:#111;border:2px solid #ddd;border-radius:10px}

/* partners */
.partners{position:absolute;left:0;top:4124px;width:1200px;height:101px;display:flex}
.partner{flex:1;border-right:1px solid var(--line);display:flex;align-items:center;justify-content:center}
.partner:last-child{border-right:0}
.partner span{display:block;width:150px;height:46px;background:#d6d6d6;border-radius:6px}

/* footer */
.site-footer{position:absolute;left:0;top:4225px;width:1200px;height:355px;background:var(--dark)}
.site-footer .brand{left:76px;top:70px;color:var(--white)}
.social{position:absolute;left:76px;top:140px;display:flex;gap:12px}
.social i{display:block;width:36px;height:36px;border-radius:50%;background:#9a9a9a}
.footer-links{position:absolute;left:76px;top:240px;font-size:12px;line-height:20px;color:#cfcfcf}
.contact-form{position:absolute;left:580px;top:40px;width:545px}
.contact-form h2{font-family:"Josefin Sans",Arial,sans-serif;font-weight:300;color:var(--orange);font-size:24px;margin-bottom:14px}
.field-row{display:flex;gap:15px;margin-bottom:17px}
.field{flex:1;height:32px;background:var(--white);font-size:12px;color:#888;padding:8px 10px}
.field.message{height:80px;margin-bottom:14px}
.contact-form .btn{height:40px;font-size:12px;padding:0 18px}
</style>
</head>
<body>

<header class="site-header">
  <div class="brand"><span class="brand-mark"></span>Brellowmo Media</div>
  <nav class="main-nav">
    <a>Home</a><a>Product</a><a>Blog</a><a>About</a><a>Contact</a>
  </nav>
  <div class="header-btn btn-login"><i></i>Member Login</div>
  <div class="header-btn btn-apps"><i></i>Sample Apps</div>
</header>

<section class="hero" role="img" aria-label="Photo of a woman holding a smartphone playing a music video">
  <div class="hero-copy">
    <h1>High Quality<br><span>Mobile Engagement</span></h1>
    <p>We engage mobile audiences with the right video content at the perfect moment.</p>
    <div class="btn">Sample Apps</div>
  </div>
</section>

<section class="welcome">
  <div class="welcome-title display">Welcome to<strong>Brellowmo Media</strong></div>
  <div class="welcome-rule"></div>
  <p class="welcome-text">Brellowmo Media exists because video consumption is trending away from TV towards mobile, &amp; because mobile media is trending away from pull consumption towards push consumption - where each user is notified of personalized content at the perfect moment.</p>
</section>

<section class="push">
  <h2 class="section-title abs center" style="top:970px">Push Video Notifications</h2>
  <p class="section-sub abs" style="top:1020px;left:400px;width:400px;text-align:center">Personalised flawless HD videos, revealed at the perfect moment, as rich media notifications.</p>

  <svg class="abs" style="left:0;top:1100px" width="1200" height="560" aria-hidden="true">
    <g stroke="#f78f20" stroke-width="1.5">
      <line x1="421" y1="146" x2="488" y2="146"/>
      <line x1="421" y1="284" x2="488" y2="284"/>
      <line x1="421" y1="421" x2="488" y2="421"/>
      <line x1="708" y1="146" x2="734" y2="146"/>
      <line x1="708" y1="284" x2="734" y2="284"/>
    </g>
    <g fill="#f78f20">
      <circle cx="421" cy="146" r="5"/><circle cx="421" cy="284" r="5"/><circle cx="421" cy="421" r="5"/>
      <circle cx="734" cy="146" r="5"/><circle cx="734" cy="284" r="5"/>
    </g>
  </svg>

  <div class="device" style="left:488px;top:1128px;width:220px;height:504px" role="img" aria-label="Smartphone showing a push video notification">
    <div class="screen"></div>
  </div>

  <p class="feature" style="left:116px;top:1220px;width:280px">Reach your mobile audience with beautiful HD thumbnails and in-notification videos.</p>
  <p class="feature" style="left:116px;top:1358px;width:280px">Content is personalised based on viewer interests and mobile viewing habits.</p>
  <p class="feature" style="left:116px;top:1506px;width:280px">Easily added to your existing apps within one hour.</p>
  <p class="feature" style="left:762px;top:1232px">Instant video playback, zero buffering, guaranteed flawless playback - even when offline.</p>
  <p class="feature" style="left:762px;top:1370px">Monetize with beautiful HD preroll or interstitial ads.</p>
</section>

<div class="divider" style="top:1700px"></div>

<section class="native">
  <h2 class="section-title abs" style="left:76px;top:1740px">Native Push Video</h2>
  <p class="section-sub abs" style="left:76px;top:1792px;width:480px">Personalised flawless HD videos, discoverable in-app, and playable even when offline.</p>

  <svg class="abs" style="left:540px;top:1860px" width="320" height="320" aria-hidden="true">
    <g stroke="#cfcfcf" stroke-width="1.5" fill="none">
      <line x1="10" y1="30" x2="110" y2="190"/>
      <line x1="10" y1="150" x2="110" y2="190"/>
      <line x1="10" y1="290" x2="110" y2="190"/>
      <line x1="110" y1="190" x2="250" y2="90"/>
      <line x1="110" y1="190" x2="260" y2="190"/>
      <line x1="110" y1="190" x2="240" y2="290"/>
    </g>
    <circle cx="110" cy="190" r="6" fill="#cfcfcf"/>
  </svg>

  <div class="abs" style="left:79px;top:1882px;width:470px;height:270px;border:1px solid #cfcfcf;background:linear-gradient(120deg,#1d2a3a,#3d4f66 55%,#111)" role="img" aria-label="In-app video trailer list shown on a tablet screen"></div>

  <div class="device" style="left:740px;top:1835px;width:300px;height:540px;transform:rotate(16deg);border-radius:44px" role="img" aria-label="Smartphone showing a list of video trailers inside an app">
    <div class="screen" style="background:linear-gradient(170deg,#2c3444,#526078 50%,#1c2230)"></div>
  </div>

  <p class="feature-list" style="left:79px;top:2205px">Guarantee your audience never gets frustrated with a poor quality mobile video streaming experience.</p>
  <p class="feature-list" style="left:375px;top:2205px;width:240px">Instant video playback, zero buffering, HD quality guaranteed - even when offline.</p>
  <p class="feature-list" style="left:79px;top:2336px">Content is personalised based on viewer interests &amp; mobile viewing habits.</p>
  <p class="feature-list" style="left:375px;top:2336px;width:240px">Monetize with beautiful HD preroll or interstitial ads.</p>
  <p class="feature-list" style="left:655px;top:2400px;width:520px">Use your existing content management &amp; hosting systems.</p>
</section>

<div class="divider" style="top:2476px"></div>

<section class="blog">
  <h2 class="section-title abs center" style="top:2528px">Latest Blog</h2>
  <p class="section-sub abs center" style="top:2582px">From Latest Upcoming Blog Posts</p>

  <figure class="blog-feature" role="img" aria-label="Photo of a hand holding a smartphone against a sunset over the sea">
    <figcaption>
      <h3>How Does “Free” Work in the Post-Mobile Era?</h3>
      <p class="meta">May 24, 2016 | By <em>Dana Whitlock</em></p>
    </figcaption>
  </figure>

  <article class="blog-card" style="left:619px;top:2638px"><h3>Scouts to Chatterlane: Ad Formats Evolve to Mobile</h3><p class="meta">May 30, 2016 | By <em>Dana Whitlock</em></p></article>
  <article class="blog-card" style="left:881px;top:2638px"><h3>Screen Ahead Forum 2016 – 5 Minute Defense</h3><p class="meta">June 30, 2016 | By <em>Dana Whitlock</em></p></article>
  <article class="blog-card" style="left:619px;top:2769px"><h3>AI drives the next level in mobile media engagement</h3><p class="meta">June 23, 2016 | By <em>Dana Whitlock</em></p></article>
  <article class="blog-card" style="left:881px;top:2769px"><h3>Closing the Gap: Smartphones vs TV</h3><p class="meta">June 28, 2016 | By <em>Dana Whitlock</em></p></article>
  <article class="blog-card" style="left:619px;top:2900px"><h3>Upfront Week + New Mobile Opportunities</h3><p class="meta">May 11, 2016 | By <em>Dana Whitlock</em></p></article>
  <article class="blog-card" style="left:881px;top:2900px"><h3>Closing the Gap: Smartphones vs TV</h3><p class="meta">June 28, 2016 | By <em>Dana Whitlock</em></p></article>
</section>

<div class="divider" style="top:3060px"></div>

<section class="team">
  <div class="team-copy">
    <h2 class="section-title">Management Team</h2>
    <p class="section-sub" style="margin-top:8px;font-size:16px">Meet Our Expert Team Members</p>
    <p>Lorem Ipsum is simply dummy text of the printing and typesetting industry. Lorem Ipsum has been the industry's standard dummy text ever since the 1500s, when an unknown printer took a galley of type and scrambled it to make a type specimen book. It has survived not only five centuries, but also the leap into electronic typesetting, remaining essentially unchanged.</p>
    <div class="btn">Meet Our Team <b>›</b></div>
  </div>
  <div class="member" style="left:650px;top:3121px;width:164px;height:164px" role="img" aria-label="Portrait photo of a team member"></div>
  <div class="member" style="left:839px;top:3166px;width:92px;height:92px" role="img" aria-label="Portrait photo of a team member"></div>
  <div class="member" style="left:610px;top:3315px;width:104px;height:104px" role="img" aria-label="Portrait photo of a team member"></div>
  <div class="member" style="left:759px;top:3306px;width:80px;height:80px" role="img" aria-label="Portrait photo of a team member"></div>
  <div class="member" style="left:872px;top:3291px;width:146px;height:146px" role="img" aria-label="Portrait photo of a team member"></div>
  <div class="member" style="left:717px;top:3438px;width:200px;height:200px" role="img" aria-label="Portrait photo of a team member"></div>
</section>

<section class="apps-band" role="img" aria-label="Photo of a young couple laughing while looking at a phone">
  <h2 class="section-title center">Sample Apps</h2>
  <p class="center" style="text-align:center">Available on Appora Store and Playvine Market</p>
  <div class="store-badge" style="left:387px"></div>
  <div class="store-badge" style="left:610px"></div>
</section>

<section class="partners" aria-label="Partners">
  <div class="partner"><span></span></div>
  <div class="partner"><span></span></div>
  <div class="partner"><span></span></div>
  <div class="partner"><span></span></div>
</section>

<footer class="site-footer">
  <div class="brand"><span class="brand-mark"></span>Brellowmo Media</div>
  <div class="social"><i></i><i></i><i></i><i></i></div>
  <div class="footer-links">
    <p>Home | Product | Blog | About | Contact</p>
    <p>© 2016 Brellowmo Media, Inc. Privacy Policy</p>
  </div>
  <form class="contact-form">
    <h2>Leave A Message</h2>
    <div class="field-row"><div class="field">Name</div><div class="field">Email</div></div>
    <div class="field-row"><div class="field">Subject</div><div class="field">Phone</div></div>
    <div class="field message">Message</div>
    <div class="btn">Send Message <b>›</b></div>
  </form>
</footer>

</body>
</html>
```